Digital Marketing company needs business cards

We are a digital marketing company providing SEO, Bidlinks and Web Development services in Australia and New Zealand. Colours and icons have to match the current website (korvalane.com.au). We'd like to keep the cards simple and clean, using the artwork we have as the background of the slider of the website (the triangles). The card should have horizontal layout.
If we could have our core services on the reverse side that'd be great:
SEO
BidLinks
Web Design&Development
Target Market(s)
Medium size to large businesses
Industry/Entity Type
Digital

```html
<!DOCTYPE html>
<html lang="en">
<head>
<meta charset="utf-8">
<title>korvalane business cards</title>
<link rel="stylesheet" href="https://fonts.googleapis.com/css2?family=Open+Sans:wght@300;400;600&display=swap">
<style>
  :root {
    --stage: #e9e9ea;
    --ink: #3f4043;
    --ink-soft: #55575b;
    --brand-blue: #1a8fc4;
    --violet-light: #c9c6ec;
    --blue-mid: #7f9ddc;
    --blue-deep: #2d4f9e;
    --card-white: #fbfcfd;
    --tint-green: #eef4e2;
    --rule: #7a7c80;
  }
  * { box-sizing: border-box; margin: 0; padding: 0; }
  html, body { width: 1200px; height: 800px; overflow: hidden; }
  body {
    background: var(--stage);
    font-family: "Open Sans", Arial, sans-serif;
    color: var(--ink);
    position: relative;
  }
  .card {
    position: absolute;
    width: 520px;
    height: 297px;
    top: 252px;
    overflow: hidden;
    box-shadow: 0 6px 18px rgba(0,0,0,0.18);
  }
  /* Reverse side */
  .card--back { left: 50px; }
  .card--back .triangle-art {
    position: absolute; inset: 0;
    background: linear-gradient(135deg, var(--violet-light) 0%, #e6e9f7 30%, var(--blue-mid) 65%, var(--blue-deep) 100%);
  }
  .card--back .brand {
    position: absolute;
    left: 150px; top: 104px;
    display: flex; align-items: center; gap: 14px;
  }
  .brand__name {
    font-weight: 400;
    font-size: 50px;
    letter-spacing: -1px;
    color: var(--ink);
    line-height: 1;
  }
  .brand__dot {
    width: 40px; height: 40px;
    border-radius: 50%;
    background: var(--brand-blue);
  }
  .services {
    position: absolute;
    left: 152px; top: 172px;
    font-size: 13px;
    color: var(--ink);
  }
  .services .sep { color: var(--brand-blue); margin: 0 6px; }

  /* Front side */
  .card--front {
    left: 630px;
    background: linear-gradient(160deg, var(--tint-green) 0%, var(--card-white) 45%, #f3f6fa 100%);
  }
  .card--front .corner-art {
    position: absolute;
    left: 0; right: 0; bottom: 0; height: 46px;
    background: linear-gradient(90deg, var(--blue-deep) 0%, var(--blue-mid) 35%, rgba(127,157,220,0.25) 70%, rgba(255,255,255,0) 100%);
  }
  .card--front .brand {
    position: absolute;
    left: 32px; top: 28px;
    display: flex; align-items: center; gap: 10px;
  }
  .card--front .brand__name { font-size: 34px; }
  .card--front .brand__dot { width: 28px; height: 28px; }
  .divider {
    position: absolute;
    left: 32px; right: 32px; top: 84px;
    height: 1px; background: var(--rule);
  }
  .person {
    position: absolute;
    right: 32px; top: 98px;
    text-align: right;
  }
  .person__name {
    font-size: 22px; font-weight: 400;
    color: var(--brand-blue);
    letter-spacing: 0.5px;
  }
  .person__role { font-size: 12px; color: var(--ink); }
  .contact {
    position: absolute;
    display: flex; gap: 8px;
    font-size: 11px; line-height: 1.5;
    color: var(--ink-soft);
  }
  .contact--address { left: 32px; top: 160px; }
  .contact--phone { left: 32px; top: 204px; }
  .contact--web { left: 250px; top: 204px; }
  .contact__icon { flex: 0 0 18px; width: 18px; height: 18px; margin-top: 1px; }
</style>
</head>
<body>

<section class="card card--back" aria-label="Card reverse">
  <div class="triangle-art" role="img" aria-label="Background of blue and violet faceted triangles"></div>
  <div class="brand">
    <span class="brand__name">korvalane</span>
    <span class="brand__dot"></span>
  </div>
  <p class="services">SEO<span class="sep">|</span>BidLinks<span class="sep">|</span>Web Design &amp; Development</p>
</section>

<section class="card card--front" aria-label="Card front">
  <div class="corner-art" role="img" aria-label="Band of blue faceted triangles along the lower edge"></div>
  <div class="brand">
    <span class="brand__name">korvalane</span>
    <span class="brand__dot"></span>
  </div>
  <div class="divider"></div>
  <div class="person">
    <p class="person__name">JONAH WEXLEY</p>
    <p class="person__role">Managing Director</p>
  </div>

  <div class="contact contact--address">
    <svg class="contact__icon" viewBox="0 0 18 18" aria-hidden="true">
      <circle cx="9" cy="9" r="9" fill="var(--brand-blue)"/>
      <path d="M9 4a3 3 0 0 0-3 3c0 2.3 3 6 3 6s3-3.7 3-6a3 3 0 0 0-3-3z" fill="#fff"/>
      <circle cx="9" cy="7" r="1.1" fill="var(--brand-blue)"/>
    </svg>
    <p>Level 3, 18 Harbour Lane<br>Ferndale, Brisbane, QLD, 4061</p>
  </div>

  <div class="contact contact--phone">
    <svg class="contact__icon" viewBox="0 0 18 18" aria-hidden="true">
      <circle cx="9" cy="9" r="9" fill="var(--brand-blue)"/>
      <rect x="6" y="4" width="6" height="10" rx="1" fill="#fff"/>
      <rect x="7" y="5.5" width="4" height="5.5" fill="var(--brand-blue)"/>
    </svg>
    <p>M : +61 41923 5067<br>O : +61 7 3185 2240</p>
  </div>

  <div class="contact contact--web">
    <svg class="contact__icon" viewBox="0 0 18 18" aria-hidden="true">
      <circle cx="9" cy="9" r="9" fill="var(--brand-blue)"/>
      <circle cx="9" cy="9" r="4.5" fill="none" stroke="#fff" stroke-width="1.2"/>
      <path d="M4.5 9h9M9 4.5c-1.6 1.5-1.6 7.5 0 9M9 4.5c1.6 1.5 1.6 7.5 0 9" fill="none" stroke="#fff" stroke-width="1"/>
    </svg>
    <p>jonah@korvalane.com.au<br>www.korvalane.com.au</p>
  </div>
</section>

</body>
</html>
```